Medical IT Business with New logo needs a fresh stationary design

First time on sketch Harbor; Thought I would give it a go.
This project is for business cards alone but we have loads of design work that needs to take place in the immediate future.

We provide IT services to the Medical Industry and value ourselves as offering a premium product to the market.

I am after a fresh, clean design using full colour 2 sided cards which includes our current colour palettes from our logo.

Card's must include:
- Logo
- Slogan
- Name
- Adress
- Email
- Phone
- Fax
- Mobile

Target Market(s)

Surgeons, High Profile Medical Personnel

Industry/Entity Type

Business

Fonts, CMYK Colours and Logo files attached.

Requirements
Must have
• Card's must include:
• - Logo
• - Slogan
• - Name
• - Adress
• - Email
• - Phone
• - Fax
• - Mobile
Nice to have
• Needs to incorporate our colour palette (attached CMYK colours)
Should not have
• Black backgrounds. Black text ok.

```html
<!DOCTYPE html>
<html lang="en">
<head>
<meta charset="utf-8">
<title>Clinova Systems – Business Cards</title>
<link rel="stylesheet" href="https://fonts.googleapis.com/css2?family=Lato:wght@300;400;700;900&display=swap">
<style>
  :root {
    --navy: #12336b;
    --blue: #1a7db3;
    --circle-blue: #1b82b8;
    --slogan: #8a9bb0;
    --ink: #2a2f36;
    --card: #ffffff;
    --backdrop: #e4e6e9;
  }
  * { box-sizing: border-box; margin: 0; padding: 0; }
  html, body {
    width: 1200px; height: 873px; overflow: hidden;
    background: var(--backdrop);
    font-family: "Lato", sans-serif;
  }
  .canvas { position: relative; width: 1200px; height: 873px; }
  .card {
    position: absolute; top: 282px;
    width: 540px; height: 309px;
    background: var(--card);
    box-shadow: 0 6px 18px rgba(0,0,0,.18);
    overflow: hidden;
  }
  .card--back { left: 40px; }
  .card--front { left: 620px; }

  /* back side */
  .back-mark {
    position: absolute; left: 250px; top: 40px;
    width: 200px; height: 165px; border-radius: 50%;
    background: var(--circle-blue);
  }
  .back-wordmark {
    position: absolute; left: 36px; top: 222px;
    color: var(--navy); font-weight: 900;
    font-size: 28px; line-height: 28px; letter-spacing: 1px;
  }
  .back-slogan {
    position: absolute; left: 38px; top: 282px;
    color: var(--slogan); font-weight: 300; font-size: 12px;
  }

  /* front side */
  .brand {
    position: absolute; left: 150px; top: 26px;
    display: flex; align-items: center; gap: 12px;
  }
  .brand__dot {
    width: 62px; height: 56px; border-radius: 50%;
    background: var(--circle-blue);
  }
  .brand__name {
    color: var(--navy); font-weight: 900;
    font-size: 24px; line-height: 23px; letter-spacing: 1px;
  }
  .brand__slogan {
    color: var(--slogan); font-weight: 300; font-size: 11.5px;
    margin-top: 3px; letter-spacing: .3px;
  }
  .person { position: absolute; right: 290px; top: 140px; text-align: right; }
  .person__name { color: var(--navy); font-weight: 900; font-size: 17px; }
  .person__title { color: var(--ink); font-size: 12.5px; margin-top: 2px; }
  .person__address {
    color: var(--blue); font-weight: 900; font-size: 14px;
    line-height: 20px; margin-top: 26px;
  }
  .divider {
    position: absolute; left: 264px; top: 130px;
    width: 2px; height: 100px;
    background: linear-gradient(to bottom, rgba(26,125,179,0), var(--blue), rgba(26,125,179,0));
  }
  .contacts { position: absolute; left: 282px; top: 126px; list-style: none; }
  .contacts li {
    display: flex; align-items: center; gap: 9px;
    height: 23px; color: var(--ink); font-size: 13.5px;
  }
  .contacts svg { width: 14px; height: 14px; fill: var(--navy); flex: none; }
  .bands { position: absolute; left: 0; top: 0; }
</style>
</head>
<body>
<main class="canvas">

  <section class="card card--back" aria-label="Card back">
    <div class="back-mark"></div>
    <div class="back-wordmark">CLINOVA<br>SYSTEMS</div>
    <div class="back-slogan">secure care, always online</div>
  </section>

  <section class="card card--front" aria-label="Card front">
    <div class="brand">
      <div class="brand__dot"></div>
      <div>
        <div class="brand__name">CLINOVA<br>SYSTEMS</div>
        <div class="brand__slogan">secure care, always online</div>
      </div>
    </div>

    <div class="person">
      <div class="person__name">Daniel Hartwell</div>
      <div class="person__title">Chief Operating Officer</div>
      <div class="person__address">42 Alder Lane<br>Brookfield, PA 15020</div>
    </div>

    <div class="divider"></div>

    <ul class="contacts">
      <li>
        <svg viewBox="0 0 16 16"><path d="M2 6c0-2 2-3 6-3s6 1 6 3v1h-3V5.5H5V7H2zM4 8h8l2 5H2z"/></svg>
        555-210-4480
      </li>
      <li>
        <svg viewBox="0 0 16 16"><path d="M4 1h8v4H4zM1 6h14v6h-3v-2H4v2H1zM5 11h6v4H5z"/></svg>
        555-210-4482
      </li>
      <li>
        <svg viewBox="0 0 16 16"><path d="M1 3h14v10H1zM2.5 4.5 8 9l5.5-4.5v1L8 10 2.5 5.5z" fill-rule="evenodd"/></svg>
        info@clinovasystems.com
      </li>
      <li>
        <svg viewBox="0 0 16 16"><path d="M9.5 2.5a3 3 0 0 1 4 4L11 9l-1-1 2.5-2.5a1.6 1.6 0 0 0-2.1-2.1L8 6 7 5zM6.5 13.5a3 3 0 0 1-4-4L5 7l1 1-2.5 2.5a1.6 1.6 0 0 0 2.1 2.1L8 10l1 1zM5.5 9.5l4-4 1 1-4 4z"/></svg>
        www.clinovasystems.com
      </li>
    </ul>

    <svg class="bands" width="540" height="309" viewBox="0 0 540 309" aria-hidden="true">
      <path d="M0,294 L338,281 L342,309 L0,309 Z" fill="var(--navy)"/>
      <path d="M340,283 Q342,264 366,262 L540,250 L540,266 Z" fill="var(--blue)"/>
    </svg>
  </section>

</main>
</body>
</html>
```